Birchline Septic Solutions

Would like to see some single sided ones but would also like to see some double sided with one sided only being the logo. Owners name is Tom Halvick. Phone number is 555-214-0387
Services are pumping, inspections, installs, and repairs

Contact Information for Business Card

555-241-0387 Tom Halvick Greenfield, OH

```html
<!DOCTYPE html>
<html lang="en">
<head>
<meta charset="UTF-8">
<title>Birchline Septic Solutions – Business Cards</title>
<link href="https://fonts.googleapis.com/css2?family=Lato:wght@400;700;900&display=swap" rel="stylesheet">
<style>
  :root {
    --stage: #2b2d30;
    --card: #1c1d1f;
    --white: #ffffff;
    --teal: #2bbfc0;
    --muted: #cfd2d4;
  }
  * { margin: 0; padding: 0; box-sizing: border-box; }
  html, body { width: 1200px; height: 952px; overflow: hidden; }
  body {
    background: var(--stage);
    font-family: "Lato", sans-serif;
    color: var(--white);
    position: relative;
  }
  .card {
    position: absolute;
    width: 540px;
    height: 310px;
    background: var(--card);
    border-radius: 18px;
    overflow: hidden;
  }
  .card--back { left: 600px; top: 150px; }
  .card--front { left: 60px; top: 500px; }

  .card__rule {
    position: absolute;
    left: 0; right: 0;
    bottom: 26px;
    height: 2px;
    background: var(--teal);
  }

  .wordmark {
    position: absolute;
    left: 0; right: 0;
    text-align: center;
    font-weight: 900;
    color: var(--white);
    text-transform: uppercase;
    line-height: 1;
  }
  .wordmark__name { display: block; font-size: 50px; letter-spacing: 1px; }
  .wordmark__sub { display: block; font-size: 17px; letter-spacing: 6px; margin-top: 8px; }

  .card--back .wordmark { top: 92px; }
  .services {
    position: absolute;
    left: 0; right: 0;
    top: 200px;
    text-align: center;
    font-size: 15px;
    letter-spacing: 1px;
    text-transform: uppercase;
  }
  .services__dot { color: var(--teal); margin: 0 6px; }

  .card--front .wordmark { top: 54px; }
  .person {
    position: absolute;
    left: 40px;
    top: 180px;
  }
  .person__name {
    font-size: 24px;
    font-weight: 700;
    color: var(--teal);
    text-transform: uppercase;
    letter-spacing: 0.5px;
  }
  .person__role { font-size: 13px; color: var(--muted); margin-top: 2px; }

  .contact {
    position: absolute;
    left: 272px;
    top: 172px;
    list-style: none;
    font-size: 14px;
    color: var(--muted);
  }
  .contact__item { display: flex; align-items: flex-start; margin-bottom: 8px; line-height: 1.3; }
  .contact__icon {
    flex: none;
    width: 18px; height: 18px;
    background: var(--teal);
    border-radius: 3px;
    margin-right: 9px;
    margin-top: 1px;
    display: flex; align-items: center; justify-content: center;
  }
  .contact__icon svg { width: 12px; height: 12px; fill: var(--white); }
</style>
</head>
<body>

  <section class="card card--back" aria-label="Card back">
    <div class="wordmark">
      <span class="wordmark__name">Birchline</span>
      <span class="wordmark__sub">Septic Solutions</span>
    </div>
    <p class="services">
      Pumping<span class="services__dot">•</span>Inspections<span class="services__dot">•</span>Installs<span class="services__dot">•</span>Repairs
    </p>
    <div class="card__rule"></div>
  </section>

  <section class="card card--front" aria-label="Card front">
    <div class="wordmark">
      <span class="wordmark__name">Birchline</span>
      <span class="wordmark__sub">Septic Solutions</span>
    </div>

    <div class="person">
      <p class="person__name">Tom Halvick</p>
      <p class="person__role">Managing Director</p>
    </div>

    <ul class="contact">
      <li class="contact__item">
        <span class="contact__icon">
          <svg viewBox="0 0 24 24"><path d="M12 2a7 7 0 0 0-7 7c0 5 7 13 7 13s7-8 7-13a7 7 0 0 0-7-7zm0 9.5A2.5 2.5 0 1 1 12 6.5a2.5 2.5 0 0 1 0 5z"/></svg>
        </span>
        <span>1820 Ridgeview Road<br>Greenfield, OH 45123</span>
      </li>
      <li class="contact__item">
        <span class="contact__icon">
          <svg viewBox="0 0 24 24"><path d="M6.6 10.8a15.1 15.1 0 0 0 6.6 6.6l2.2-2.2a1 1 0 0 1 1-.25 11.4 11.4 0 0 0 3.6.57 1 1 0 0 1 1 1V20a1 1 0 0 1-1 1A17 17 0 0 1 3 4a1 1 0 0 1 1-1h3.5a1 1 0 0 1 1 1c0 1.25.2 2.45.57 3.57a1 1 0 0 1-.25 1z"/></svg>
        </span>
        <span>555-241-0387</span>
      </li>
      <li class="contact__item">
        <span class="contact__icon">
          <svg viewBox="0 0 24 24"><path d="M5 3l14 7-6 2-2 6z"/></svg>
        </span>
        <span>www.birchlineseptic.com</span>
      </li>
    </ul>

    <div class="card__rule"></div>
  </section>

</body>
</html>
```